" Sou formada ha 12 anos e ha 3 anos inaugurei a clinica onde realizo atendimento em todas as especilidades odontologicas. Sou responsavel por fazer as avaliacoes e pelo tratamento ortodontico, trouxe outros colegas para trabalharem comigo que possuem outras especialidades como: periodontia, estetica, implantodontia... O objetivo e promover tratamento qualificado aos pacientes que nos procuram. Todos os profissionais possuem titulo de especialista e sao formados ha mais de 10 anos. "

```html
<!DOCTYPE html>
<html lang="pt">
<head>
<meta charset="utf-8">
<title>Morvani – Pasta institucional</title>
<link rel="stylesheet" href="https://fonts.googleapis.com/css2?family=Cinzel:wght@500&display=swap">
<style>
  :root {
    --backdrop: #ecebe8;
    --panel-grey: #d7d8da;
    --panel-white: #ffffff;
    --shadow-grey: #8a8c90;
    --brand-orange: #f08a32;
    --brand-navy: #1f2f5c;
    --brand-text: #5d6270;
    --fold-line: #c9cacc;
  }
  html, body {
    margin: 0;
    width: 1200px;
    height: 1200px;
    overflow: hidden;
    background: var(--backdrop);
  }
  .folder {
    position: absolute;
    left: 185px;
    top: 195px;
    width: 830px;
    height: 810px;
    display: flex;
    box-shadow: 0 10px 30px rgba(0,0,0,0.18);
  }
  .folder__inner-left {
    position: relative;
    width: 415px;
    height: 100%;
    background: var(--panel-grey);
    border-right: 1px solid var(--fold-line);
    overflow: hidden;
  }
  .folder__inner-right {
    position: relative;
    width: 415px;
    height: 100%;
    background: var(--panel-white);
  }
  .accent-band {
    position: absolute;
    left: 0;
    top: 440px;
    width: 100%;
    height: 56px;
    background: linear-gradient(90deg, var(--brand-orange) 0%, var(--brand-orange) 45%, var(--brand-navy) 55%, var(--brand-navy) 100%);
  }
  .shade-band {
    position: absolute;
    left: 0;
    top: 500px;
    width: 100%;
    height: 80px;
    background: linear-gradient(180deg, var(--panel-grey) 0%, var(--shadow-grey) 100%);
  }
  .pocket {
    position: absolute;
    left: 0;
    top: 0;
    width: 415px;
    height: 810px;
  }
  .pocket__name {
    position: absolute;
    left: 40px;
    top: 700px;
    width: 150px;
    text-align: center;
    transform: rotate(180deg);
    font-family: "Cinzel", serif;
    font-weight: 500;
    font-size: 17px;
    letter-spacing: 1px;
    color: var(--brand-text);
  }
  .brand {
    position: absolute;
    left: 0;
    top: 270px;
    width: 100%;
    display: flex;
    justify-content: center;
    align-items: center;
    gap: 10px;
  }
  .brand__dot {
    width: 14px;
    height: 14px;
    border-radius: 50%;
    background: var(--brand-orange);
  }
  .brand__name {
    font-family: "Cinzel", serif;
    font-weight: 500;
    font-size: 34px;
    letter-spacing: 2px;
    color: var(--brand-text);
  }
</style>
</head>
<body>
  <main class="folder">
    <section class="folder__inner-left">
      <div class="accent-band" role="img" aria-label="Faixa decorativa em laranja e azul-marinho"></div>
      <div class="shade-band"></div>
      <svg class="pocket" viewBox="0 0 415 810" aria-hidden="true">
        <polygon points="0,580 300,580 345,640 345,810 0,810" fill="#ffffff"/>
        <line x1="300" y1="580" x2="345" y2="640" stroke="#d2d3d5" stroke-width="1"/>
      </svg>
      <div class="pocket__name">MORVANI</div>
    </section>
    <section class="folder__inner-right">
      <div class="brand">
        <span class="brand__dot"></span>
        <span class="brand__name">MORVANI</span>
      </div>
    </section>
  </main>
</body>
</html>
```